New Business Card for Web Design/Internet Marketing Company

Looking for a great looking new business card. We are a 10 year old web design, internet marketing and website management company that works mostly with small businesses.

Our new card needs to better match the colors and style of our website, be bold, extremely usable and slightly edgy.

Target Market(s)

Small/Medium businesses that have websites

Industry/Entity Type

Internet

Requirements
Must have
• Front and back design, full color, rounded corners please

Must use the colors/style of our website (JPG provided)

INFO FOR CARDS (as readable as possible please)
Mark Pellow
President/CEO
mark@brightlanesites.com
Phone: 520-481-7093
Toll Free: 866-481-7093
Address: 4315 E. Kestrel Ave. Ste. 140, Tucson, AZ 85733

THINGS I WANT TO PROMOTE (if there is room):
1. Our Website - www.brightlanesites.com

2. Social Media
Chirper: @brightlanesites
Friendbook: www.friendbook.com/brightlanesites

3. Our Services
Web Design
Internet Marketing
Website Management

```html
<!DOCTYPE html>
<html lang="en">
<head>
<meta charset="utf-8">
<title>Bright Lane Sites — Business Card</title>
<link rel="stylesheet" href="https://fonts.googleapis.com/css2?family=Ubuntu:wght@400;500;700&display=swap">
<style>
  :root {
    --canvas: #efece8;
    --card: #ffffff;
    --blue: #5aa8f0;
    --teal: #19bcc6;
    --orange: #f26a21;
    --watermark: rgba(25, 188, 198, 0.14);
    --shadow: 0 6px 18px rgba(0, 0, 0, 0.18);
  }
  * { box-sizing: border-box; margin: 0; padding: 0; }
  html, body {
    width: 1200px; height: 1200px; overflow: hidden;
    background: var(--canvas);
    font-family: "Ubuntu", sans-serif;
  }
  .sheet { position: relative; width: 1200px; height: 1200px; }
  .card {
    position: absolute; left: 250px; width: 700px; height: 400px;
    background: var(--card); border-radius: 14px; box-shadow: var(--shadow);
    overflow: hidden; color: var(--blue);
  }
  .card--front { top: 130px; }
  .card--back { top: 660px; }

  .brand {
    display: flex; align-items: center; gap: 12px;
    font-weight: 700; color: var(--teal); white-space: nowrap;
  }
  .brand__dot {
    width: 34px; height: 34px; border-radius: 50%; background: var(--orange);
    flex: none;
  }
  .card--front .brand { position: absolute; left: 36px; top: 48px; font-size: 30px; }

  .watermark {
    position: absolute; left: 150px; top: 150px;
    font-size: 48px; font-weight: 700; color: var(--watermark); white-space: nowrap;
  }

  .person {
    position: absolute; right: 40px; top: 34px;
    font-size: 17px; line-height: 1.35; font-style: normal;
  }
  .person__name { font-weight: 700; }

  .band {
    position: absolute; left: 0; right: 0; top: 318px; height: 12px;
    background: var(--blue);
  }
  .contact-line {
    position: absolute; left: 24px; right: 24px; top: 344px;
    font-size: 13.5px; white-space: nowrap;
  }

  .card--back .brand {
    position: absolute; left: 50%; top: 50%; transform: translate(-50%, -60%);
    font-size: 46px; gap: 16px;
  }
  .card--back .brand__dot { width: 52px; height: 52px; }
  .site-url { position: absolute; left: 26px; top: 24px; font-size: 16px; }
  .social {
    position: absolute; right: 30px; bottom: 90px; font-size: 16px; line-height: 1.45;
  }
  .social dt { display: inline; }
  .social dd { display: inline; margin-left: 6px; }
  .services {
    position: absolute; left: 26px; bottom: 22px; list-style: none;
    font-size: 16px; line-height: 1.4;
  }
</style>
</head>
<body>
<main class="sheet">
  <section class="card card--front" aria-label="Card front">
    <div class="brand"><span class="brand__dot"></span>Bright Lane Sites</div>
    <div class="watermark" aria-hidden="true">Bright Lane Sites</div>
    <address class="person">
      <div class="person__name">Mark Pellow</div>
      <div>President/CEO</div>
      <div>mark@brightlanesites.com</div>
    </address>
    <div class="band"></div>
    <p class="contact-line">Phone: 520-481-7093, Toll Free: 866-481-7093, Address: 4315 E. Kestrel Ave. Ste. 140, Tucson, AZ 85733</p>
  </section>

  <section class="card card--back" aria-label="Card back">
    <p class="site-url">www.brightlanesites.com</p>
    <div class="brand"><span class="brand__dot"></span>Bright Lane Sites</div>
    <dl class="social">
      <div><dt>Chirper:</dt><dd>@brightlanesites</dd></div>
      <div><dt>Friendbook:</dt><dd>www.friendbook.com/brightlanesites</dd></div>
    </dl>
    <ul class="services">
      <li>Web Design</li>
      <li>Website Management</li>
      <li>Internet Marketing</li>
    </ul>
  </section>
</main>
</body>
</html>
```